Eye catching while remaining subtle, stylish and professional

Plover Works are a Heatpump and Air Conditioning Company. I would like stationary that would be suitable to use for letters, quoting invoicing. The final design should communicate a trade/service type industry that is clean and professional

I would like the designer to also offer a Business card option as well.

Details should include company logo as attached. Company details. Name, Address, Phone, Email and Website. You can use generic details until a final design is chosen

Target Market(s)

Trade/Service Industry

Industry/Entity Type

Air Conditioning

Requirements
Must have
• LOGO, Company contact details
Nice to have
• Watermark

```html
<!DOCTYPE html>
<html lang="en">
<head>
<meta charset="utf-8">
<title>Plover Works Stationery</title>
<link rel="stylesheet" href="https://fonts.googleapis.com/css2?family=Jost:wght@400;500;600&display=swap">
<style>
  :root {
    --backdrop: #d5d5d5;
    --paper: #f7f7f7;
    --paper-edge: #e2e2e2;
    --band: #e4e4e4;
    --brand: #2f9fd6;
    --brand-deep: #0a84c2;
    --brand-light: #b5d9ea;
    --ink: #4a4a4a;
    --ink-soft: #8a8a8a;
    --white: #ffffff;
  }
  * { margin: 0; padding: 0; box-sizing: border-box; }
  html, body { width: 1200px; height: 969px; overflow: hidden; }
  body {
    background: var(--backdrop);
    font-family: "Jost", sans-serif;
    color: var(--ink);
    position: relative;
  }
  .sheet { position: absolute; background: var(--paper); box-shadow: 0 1px 3px rgba(0,0,0,.18); overflow: hidden; }
  .pattern-band { position: absolute; left: 0; right: 0; bottom: 0; background: var(--band); }
  .wordmark { position: absolute; color: var(--brand); font-weight: 500; line-height: 1; }
  .wordmark .name { display: block; letter-spacing: .02em; }
  .wordmark .sub { display: block; letter-spacing: .55em; margin-top: 5px; }
  .small { position: absolute; font-size: 6px; line-height: 8.5px; color: var(--ink); }

  /* Letterhead */
  .letterhead { left: 162px; top: 65px; width: 408px; height: 590px; }
  .letterhead .wordmark { left: 38px; top: 48px; }
  .letterhead .wordmark .name { font-size: 31px; }
  .letterhead .wordmark .sub { font-size: 7px; }
  .letterhead .contact { left: 295px; top: 45px; }
  .contact-line { display: flex; align-items: center; gap: 3px; }
  .contact-line svg { width: 6px; height: 6px; flex: none; }
  .letterhead .date { left: 38px; top: 110px; }
  .letterhead .recipient { left: 38px; top: 121px; }
  .letterhead .body { left: 38px; top: 204px; width: 333px; text-align: justify; }
  .letterhead .body p { margin-bottom: 8.5px; }
  .letterhead .body .salutation { font-weight: 600; margin-bottom: 6px; }
  .letterhead .closing { left: 38px; top: 382px; }
  .letterhead .closing strong { font-weight: 600; }
  .signature { position: absolute; left: 90px; top: 372px; width: 80px; height: 46px; background: linear-gradient(120deg, rgba(60,70,180,.12), rgba(60,70,180,.04)); }
  .fold-mark { position: absolute; left: 0; width: 18px; height: 1px; background: var(--paper-edge); }
  .letterhead .pattern-band { height: 28px; }

  /* Folder */
  .folder { left: 604px; top: 63px; width: 444px; height: 592px; background: linear-gradient(180deg, var(--brand-light) 0%, #6ab6de 45%, var(--brand-deep) 100%); border-radius: 3px; }
  .folder .spine { position: absolute; left: 10px; top: 0; bottom: 0; width: 8px; border-left: 1px solid rgba(255,255,255,.35); border-right: 1px solid rgba(0,60,110,.18); }
  .folder .wordmark { left: 0; right: 0; top: 87px; text-align: center; color: var(--white); }
  .folder .wordmark .name { font-size: 48px; }
  .folder .wordmark .sub { font-size: 10px; margin-top: 9px; padding-left: .55em; }

  /* Business cards */
  .card-front { left: 54px; top: 689px; width: 175px; height: 97px; }
  .card-front .wordmark { left: 13px; top: 30px; }
  .card-front .wordmark .name { font-size: 19px; }
  .card-front .wordmark .sub { font-size: 4.5px; margin-top: 3px; }
  .card-front .divider { position: absolute; left: 99px; top: 16px; width: 1px; height: 56px; background: var(--paper-edge); }
  .card-front .details { left: 105px; top: 17px; font-size: 4.5px; line-height: 6px; }
  .card-front .details .person { color: var(--brand); font-weight: 600; font-size: 5px; }
  .card-front .details .role { margin-bottom: 3px; color: var(--ink-soft); }
  .card-front .details .contact-line svg { width: 4px; height: 4px; }
  .card-front .details .address { margin-top: 3px; }
  .card-front .pattern-band { height: 15px; }
  .card-back { left: 54px; top: 806px; width: 175px; height: 97px; background: linear-gradient(180deg, var(--brand-light), var(--brand-deep)); }
  .card-back .wordmark { left: 0; right: 0; top: 36px; text-align: center; color: var(--white); }
  .card-back .wordmark .name { font-size: 19px; }
  .card-back .wordmark .sub { font-size: 4.5px; margin-top: 3px; padding-left: .55em; }

  /* Envelopes */
  .envelope-front { left: 265px; top: 689px; width: 388px; height: 214px; }
  .envelope-front .wordmark { left: 22px; top: 20px; }
  .envelope-front .wordmark .name { font-size: 30px; }
  .envelope-front .wordmark .sub { font-size: 7px; }
  .envelope-front .return-address { left: 22px; top: 74px; }
  .envelope-front .pattern-band { height: 30px; }
  .envelope-back { left: 727px; top: 689px; width: 427px; height: 214px; }
  .envelope-back svg.flap { position: absolute; left: 0; top: 0; }
</style>
</head>
<body>

<svg width="0" height="0" style="position:absolute">
  <defs>
    <symbol id="icon-phone" viewBox="0 0 10 10"><rect width="10" height="10" rx="2" fill="#2f9fd6"/><path d="M3 2.5c-.6.4-.7 1.2-.3 2 .6 1.3 1.6 2.3 2.8 2.9.8.4 1.5.3 1.9-.3L6.5 6 5.8 6.5C5 6.1 4.3 5.4 3.9 4.6L4.4 3.9z" fill="#fff"/></symbol>
    <symbol id="icon-mail" viewBox="0 0 10 10"><rect width="10" height="10" rx="2" fill="#2f9fd6"/><rect x="2" y="3" width="6" height="4" fill="none" stroke="#fff" stroke-width=".8"/><path d="M2 3l3 2.3L8 3" fill="none" stroke="#fff" stroke-width=".8"/></symbol>
    <symbol id="icon-web" viewBox="0 0 10 10"><rect width="10" height="10" rx="2" fill="#2f9fd6"/><circle cx="5" cy="5" r="2.8" fill="none" stroke="#fff" stroke-width=".8"/><path d="M2.2 5h5.6M5 2.2c1.4 1.6 1.4 4 0 5.6M5 2.2c-1.4 1.6-1.4 4 0 5.6" fill="none" stroke="#fff" stroke-width=".6"/></symbol>
  </defs>
</svg>

<!-- Letterhead -->
<section class="sheet letterhead">
  <div class="wordmark"><span class="name">PLOVER</span><span class="sub">WORKS</span></div>
  <div class="small contact">
    <div>12/58 Harlow Road</div>
    <div>Ashby, VIC 3172</div>
    <div class="contact-line"><svg><use href="#icon-phone"/></svg>009 71 44 00 62</div>
    <div class="contact-line"><svg><use href="#icon-mail"/></svg>info@ploverworks.com</div>
    <div class="contact-line"><svg><use href="#icon-web"/></svg>www.ploverworks.com</div>
  </div>
  <div class="small date">30.02.2015</div>
  <div class="small recipient">
    <div>Recipient's name</div>
    <div>Lindenweg 4</div>
    <div>10419 Berlin</div>
    <div>Germany</div>
  </div>
  <div class="small body">
    <p class="salutation">Dear sir,</p>
    <p>Thank you for considering us for your heating and cooling needs. Our team installs, services and repairs heat pumps and air conditioning systems for homes and businesses across the region. Every job begins with a careful site visit so that the system we recommend suits the space, the climate and your budget.</p>
    <p>Attached you will find our quote for the supply and installation of a new ducted unit, including removal of the old equipment, all wiring and pipework, and a full commissioning check once the work is done. Prices are fixed for thirty days from the date of this letter, and our standard warranty covers parts and labour for five years. Should you need any detail changed, simply let us know.</p>
    <p>Our technicians are fully licensed and carry the tools and parts needed to finish most jobs in a single visit. We keep your home clean while we work and explain how to get the best from your new system before we leave.</p>
    <p>We look forward to working with you. If you have any questions about this quote or would like to book an installation date, please call our office or reply by email and a member of our team will be in touch within one working day.</p>
  </div>
  <div class="small closing">
    <div>Yours Sincerely,</div>
    <div><strong>Nora Vell</strong></div>
  </div>
  <div class="signature" role="img" aria-label="Handwritten signature in blue ink"></div>
  <div class="fold-mark" style="top:265px"></div>
  <div class="fold-mark" style="top:420px"></div>
  <div class="pattern-band" role="img" aria-label="Light grey band with a repeating frost-branch pattern"></div>
</section>

<!-- Presentation folder -->
<section class="sheet folder">
  <div class="spine"></div>
  <div class="wordmark"><span class="name">PLOVER</span><span class="sub">WORKS</span></div>
</section>

<!-- Business card front -->
<section class="sheet card-front">
  <div class="wordmark"><span class="name">PLOVER</span><span class="sub">WORKS</span></div>
  <div class="divider"></div>
  <div class="small details">
    <div class="person">SAM CORRIN</div>
    <div class="role">General Manager</div>
    <div class="contact-line"><svg><use href="#icon-phone"/></svg>009 71 44 00 62</div>
    <div class="contact-line"><svg><use href="#icon-mail"/></svg>info@ploverworks.com</div>
    <div class="contact-line"><svg><use href="#icon-web"/></svg>www.ploverworks.com</div>
    <div class="address">12/58 Harlow Road<br>Ashby, VIC 3172</div>
  </div>
  <div class="pattern-band" role="img" aria-label="Light grey band with a repeating frost-branch pattern"></div>
</section>

<!-- Business card back -->
<section class="sheet card-back">
  <div class="wordmark"><span class="name">PLOVER</span><span class="sub">WORKS</span></div>
</section>

<!-- Envelope front -->
<section class="sheet envelope-front">
  <div class="wordmark"><span class="name">PLOVER</span><span class="sub">WORKS</span></div>
  <div class="small return-address">
    <div>12/58 Harlow Road</div>
    <div>Ashby, VIC 3172</div>
  </div>
  <div class="pattern-band" role="img" aria-label="Light grey band with a repeating frost-branch pattern"></div>
</section>

<!-- Envelope back -->
<section class="sheet envelope-back">
  <svg class="flap" width="427" height="62" viewBox="0 0 427 62">
    <defs>
      <linearGradient id="flap-fill" x1="0" y1="0" x2="0" y2="1">
        <stop offset="0" stop-color="#63bde6"/>
        <stop offset="1" stop-color="#1f98d4"/>
      </linearGradient>
    </defs>
    <polygon points="0,0 427,0 413,59 14,59" fill="url(#flap-fill)"/>
    <circle cx="213" cy="31" r="7" fill="#ffffff"/>
  </svg>
</section>

</body>
</html>
```